Zielgruppe
Was machen wir: Datenschutz und Informationssicherheit als Dienstleistung.
Zielgruppe: Mittelständische Unternehmenskunden 500 -5000 Mitarbeiter
Aufgabenstellung
Wir benötigen eine neue Powerpoint Vorlage. Die alte Vorlage ist nicht mehr zeitgemäß.
Format: DIN 16:9
Standardschriftart: Calibri
Zielgruppe: Mittleres und gehobenes Management
CI: Unsere Farben können auf unserer Webseite eingesehen werden.

```html
<!DOCTYPE html>
<html lang="de">
<head>
<meta charset="utf-8">
<title>Inhalt</title>
<link rel="stylesheet" href="https://fonts.googleapis.com/css2?family=Carlito:wght@400;700&display=swap">
<style>
  :root {
    --navy: #3e4f8a;
    --navy-light: #5566a3;
    --orange: #f5841f;
    --hex-1: #ee7f11;
    --hex-2: #ea8c2c;
    --hex-3: #eb983b;
    --hex-4: #ebaf70;
    --hex-5: #ebc093;
    --white: #ffffff;
  }
  html, body {
    margin: 0;
    padding: 0;
    width: 1200px;
    height: 675px;
    overflow: hidden;
    background: var(--navy);
  }
  .slide {
    position: relative;
    width: 1200px;
    height: 675px;
    overflow: hidden;
    font-family: "Carlito", "Calibri", sans-serif;
    color: var(--white);
  }
  .backdrop {
    position: absolute;
    inset: 0;
    background:
      linear-gradient(176deg, transparent 30%, rgba(120,140,200,0.35) 33%, transparent 36%),
      linear-gradient(172deg, transparent 58%, rgba(90,110,180,0.25) 63%, transparent 68%),
      linear-gradient(165deg, rgba(110,90,170,0.35) 0%, transparent 14%),
      linear-gradient(160deg, transparent 75%, rgba(70,120,190,0.35) 86%, transparent 95%),
      var(--navy);
  }
  .edge {
    position: absolute;
    top: 0;
    bottom: 0;
    width: 12px;
    background: var(--orange);
  }
  .edge--left { left: 0; }
  .edge--right { right: 0; }
  .title {
    position: absolute;
    left: 62px;
    top: 36px;
    margin: 0;
    font-size: 46px;
    font-weight: 700;
    letter-spacing: 9px;
    color: var(--orange);
    line-height: 1;
  }
  .title-rule {
    position: absolute;
    left: 12px;
    top: 92px;
    width: 290px;
    height: 2px;
    background: var(--orange);
  }
  .honeycomb {
    position: absolute;
    left: 0;
    top: 0;
  }
  .step-label {
    position: absolute;
    width: 120px;
    margin-left: -60px;
    text-align: center;
    font-size: 23px;
    font-weight: 700;
    line-height: 25px;
  }
  .summary {
    position: absolute;
    left: 62px;
    top: 518px;
  }
  .summary h2 {
    margin: 0;
    font-size: 23px;
    font-weight: 700;
    line-height: 28px;
  }
  .summary p {
    margin: 2px 0 0;
    font-size: 22.5px;
    line-height: 31px;
  }
  .brand {
    position: absolute;
    right: 44px;
    bottom: 28px;
    font-size: 20px;
    font-weight: 700;
    color: #c9d0e6;
  }
</style>
</head>
<body>
<div class="slide">
  <div class="backdrop" role="img" aria-label="Dunkelblauer Hintergrund mit weichen hellen Lichtstreifen"></div>
  <div class="edge edge--left"></div>
  <div class="edge edge--right"></div>

  <h1 class="title">INHALT</h1>
  <div class="title-rule"></div>

  <svg class="honeycomb" width="1200" height="675" viewBox="0 0 1200 675" aria-hidden="true">
    <defs>
      <polygon id="hex" points="57,0 171,0 228,99 171,198 57,198 0,99"/>
      <g id="dots" fill="#ffffff">
        <rect x="-26" y="-5.5" width="11" height="11" rx="3"/>
        <rect x="-5.5" y="-5.5" width="11" height="11" rx="3"/>
        <rect x="15" y="-5.5" width="11" height="11" rx="3"/>
      </g>
    </defs>

    <use href="#hex" x="71" y="151" fill="var(--hex-1)"/>
    <use href="#hex" x="251" y="254" fill="var(--hex-2)"/>
    <use href="#hex" x="432" y="358" fill="var(--hex-3)"/>
    <use href="#hex" x="613" y="255" fill="var(--hex-4)"/>
    <use href="#hex" x="793" y="358" fill="var(--hex-5)"/>

    <g class="lock-icon">
      <path d="M166 230 V212 a21 21 0 0 1 42 0 V230" fill="none" stroke="#ffffff" stroke-width="10"/>
      <rect x="142" y="226" width="91" height="78" rx="10" fill="#ffffff"/>
      <circle cx="187" cy="253" r="9" fill="var(--hex-1)"/>
      <rect x="184" y="253" width="6.5" height="32" rx="3.2" fill="var(--hex-1)"/>
    </g>

    <use href="#dots" x="365" y="364"/>
    <use href="#dots" x="546" y="461"/>
    <use href="#dots" x="727" y="358"/>
    <use href="#dots" x="908" y="458"/>
  </svg>

  <div class="step-label" style="left:184px; top:357px;">Lorem<br>ipsum</div>
  <div class="step-label" style="left:364px; top:197px;">Lorem<br>ipsum</div>
  <div class="step-label" style="left:545px; top:301px;">Lorem<br>ipsum</div>
  <div class="step-label" style="left:726px; top:459px;">Lorem<br>ipsum</div>
  <div class="step-label" style="left:905px; top:562px;">Lorem<br>ipsum</div>

  <div class="summary">
    <h2>LOREM IPSUM</h2>
    <p>Lorem ipsum dolor sit amet,<br>consectetur adipiscing elit, sed do<br>do eiusmod tempor incididunt ut</p>
  </div>

  <div class="brand">Valtor</div>
</div>
</body>
</html>
```